Corporate Branding - Web and Print

A UK based company will like to use an existing logo to create branding materials for all marketing related documents, including business card, prints, letterhead, Website, Twitter, Facebook, Instagram logo etc. This company serves high-end clientele in the fashion, health and wellness and as such high quality and class is of utmost importance.
Where the logo can be modernised without losing its character then experiment. The main thing is to have a corporate branding which can be used later for brochures, Business Plan infographics.
The prominent colour within the organisation is burnt orange with no secondary colour. However if you believe a secondary colour is needed then use it, otherwise keep it simple and classy. Any chosen colours have to match perfectly.
Target Market(s)
High net worth individuals
Industry/Entity Type
Health And Wellness
Contact Information for Business Card
classy
Look and feel
Each slider illustrates characteristics of the customer's brand and the style your logo design should communicate.

```html
<!DOCTYPE html>
<html lang="en">
<head>
<meta charset="utf-8">
<title>Vorelle Business Card</title>
<link rel="stylesheet" href="https://fonts.googleapis.com/css2?family=Arimo:wght@400;700&display=swap">
<style>
  :root {
    --stage: #262627;
    --card-dark: #3d3d3f;
    --card-light: #f4f4f4;
    --band-grey: #4a4a4c;
    --burnt-orange: #e58a1f;
    --text-light: #e9e9e9;
  }
  * { margin: 0; padding: 0; box-sizing: border-box; }
  html, body { width: 1200px; height: 997px; overflow: hidden; }
  body {
    background: var(--stage);
    font-family: "Arimo", Arial, sans-serif;
    position: relative;
  }
  .card {
    position: absolute;
    width: 510px;
    height: 292px;
    overflow: hidden;
    box-shadow: 0 14px 30px rgba(0,0,0,0.45);
  }
  /* Front */
  .card-front { left: 60px; top: 352px; background: var(--card-dark); }
  .front-disc {
    position: absolute;
    width: 330px; height: 330px;
    right: -70px; top: -150px;
    border-radius: 50%;
    background: var(--burnt-orange);
  }
  .wordmark {
    display: flex; align-items: center; gap: 10px;
    color: var(--burnt-orange);
    font-weight: 700;
    letter-spacing: 1px;
  }
  .wordmark .dot { border-radius: 50%; background: var(--burnt-orange); }
  .front-mark { position: absolute; left: 34px; bottom: 34px; font-size: 30px; }
  .front-mark .dot { width: 28px; height: 28px; }

  /* Back */
  .card-back { left: 630px; top: 352px; background: var(--card-dark); }
  .back-top {
    position: absolute; inset: 0 0 auto 0; height: 128px;
    background: var(--card-light);
    display: flex; align-items: center; justify-content: center;
  }
  .back-mark { font-size: 38px; }
  .back-mark .dot { width: 34px; height: 34px; }
  .back-band { position: absolute; left: 0; right: 0; top: 128px; height: 8px; background: var(--band-grey); }
  .back-rule { position: absolute; left: 0; right: 0; top: 136px; height: 3px; background: var(--burnt-orange); }
  .notch { position: absolute; left: 40px; top: 139px; }
  .person { position: absolute; left: 34px; top: 158px; }
  .person-name { color: var(--burnt-orange); font-size: 17px; }
  .person-role { color: var(--text-light); font-size: 12px; margin-top: 2px; }
  .contacts { position: absolute; left: 34px; top: 214px; list-style: none; }
  .contacts li {
    display: flex; align-items: center; gap: 10px;
    color: var(--text-light); font-size: 13px; height: 21px;
  }
  .contacts svg { width: 12px; height: 12px; flex: none; }
  .square-icon { width: 10px; height: 10px; background: var(--burnt-orange); flex: none; margin: 0 1px; }
  .office { position: absolute; right: 30px; top: 170px; text-align: right; }
  .office .dot {
    display: inline-block; width: 54px; height: 54px;
    border-radius: 50%; background: var(--burnt-orange);
    margin-right: 40px;
  }
  .office-address { color: var(--burnt-orange); font-size: 12.5px; line-height: 1.3; margin-top: 8px; }
</style>
</head>
<body>
  <section class="card card-front" aria-label="Business card front">
    <div class="front-disc"></div>
    <div class="wordmark front-mark"><span class="dot"></span>VORELLE</div>
  </section>

  <section class="card card-back" aria-label="Business card back">
    <div class="back-top">
      <div class="wordmark back-mark"><span class="dot"></span>VORELLE</div>
    </div>
    <div class="back-band"></div>
    <div class="back-rule"></div>
    <svg class="notch" width="14" height="8" viewBox="0 0 14 8"><polygon points="0,0 14,0 7,8" fill="var(--burnt-orange)"/></svg>

    <div class="person">
      <p class="person-name">Marcus Hale</p>
      <p class="person-role">CEO &amp; Managing Director</p>
    </div>

    <ul class="contacts">
      <li>
        <svg viewBox="0 0 24 24"><path fill="var(--burnt-orange)" d="M6.6 10.8a15 15 0 0 0 6.6 6.6l2.2-2.2a1 1 0 0 1 1-.25 11.4 11.4 0 0 0 3.6.57 1 1 0 0 1 1 1V20a1 1 0 0 1-1 1A17 17 0 0 1 3 4a1 1 0 0 1 1-1h3.5a1 1 0 0 1 1 1c0 1.25.2 2.45.57 3.57a1 1 0 0 1-.25 1z"/></svg>
        0400 318 642
      </li>
      <li><span class="square-icon"></span>/harrowlane.com.au</li>
      <li>
        <svg viewBox="0 0 24 24"><rect x="2" y="5" width="20" height="14" fill="var(--burnt-orange)"/><polyline points="2,5 12,13 22,5" fill="none" stroke="var(--card-dark)" stroke-width="2"/></svg>
        info@harrowlane.com.au
      </li>
    </ul>

    <div class="office">
      <span class="dot"></span>
      <p class="office-address">22 Meridian Row near<br>Eastgate Circle, India.</p>
    </div>
  </section>
</body>
</html>
```